Brightpath Wellness Referral Program

We have recently started a referral program for our clinics and we need a postcard that we can hand our to clients to let them know about the new program.
We are looking for a 4x6" card design that highlights our incentive referral program while visually either showing some of the services we offer, or, conveying a message of health, community, family, etc.
The details of our referral program can be found at:
https://brightpathwellness.ca/about/refer-a-friend.html
We would also like to see somewhere on the card, 2 lines for:
1) Your name: ( new clients name)
2) Referred by: __________
The card can be single or double sided, whatever looks best for design purposes.
Target Market(s)
Ages 20-50, equal men and women
Look and feel
Each slider illustrates characteristics of the customer's brand and the style your logo design should communicate.

```html
<!DOCTYPE html>
<html lang="en">
<head>
<meta charset="utf-8">
<title>Brightpath Wellness Referral Program Postcard</title>
<link href="https://fonts.googleapis.com/css2?family=Anton&family=Montserrat:wght@400;600;700&family=Lexend:wght@700&family=Roboto+Condensed:wght@300;400&display=swap" rel="stylesheet">
<style>
  :root {
    --bg: #7d7d7d;
    --card: #ffffff;
    --ink: #1e1e1e;
    --blue: #0866a8;
    --grey-box: #8a8a8a;
    --grey-band: #959595;
    --band-text: #f4f4f4;
    --rule: #4a4a4a;
  }
  * { box-sizing: border-box; margin: 0; padding: 0; }
  html, body { width: 1200px; height: 900px; overflow: hidden; background: var(--bg); }
  .postcard {
    position: absolute; left: 60px; top: 90px;
    width: 1080px; height: 720px;
    background: var(--card);
    padding: 44px 50px 40px;
    font-family: "Montserrat", sans-serif;
    color: var(--ink);
    box-shadow: 0 6px 18px rgba(0,0,0,.25);
  }
  .header { display: flex; justify-content: space-between; align-items: flex-start; }
  .announce { font-family: "Anton", sans-serif; font-size: 27px; letter-spacing: .3px; line-height: 1; text-transform: uppercase; }
  .program-title { font-family: "Anton", sans-serif; font-size: 66px; color: var(--blue); line-height: 1.02; letter-spacing: 1px; text-transform: uppercase; }
  .tagline {
    font-family: "Lexend", sans-serif; font-weight: 700; font-size: 38px; line-height: 1.05;
    color: var(--ink); text-shadow: 2px 3px 4px rgba(0,0,0,.2); margin-top: -4px; margin-right: 40px;
  }
  .tagline span { display: block; }
  .tagline .indent { padding-left: 28px; }
  .intro { margin-top: 16px; font-size: 17px; line-height: 1.45; }
  .intro p + p { margin-top: 4px; }
  .offers { display: flex; gap: 26px; margin-top: 20px; }
  .offer { display: flex; align-items: stretch; flex: 1; }
  .offer-amount {
    background: var(--grey-box); color: #fff; width: 96px;
    display: flex; flex-direction: column; align-items: center; justify-content: center;
    margin-top: 22px; padding: 6px 0; border: 3px solid #fff; outline: 1px solid var(--grey-box);
  }
  .offer-amount .earn { font-size: 18px; font-weight: 400; letter-spacing: 1px; }
  .offer-amount .value { font-family: "Anton", sans-serif; font-size: 36px; line-height: 1; }
  .offer-text {
    background: var(--blue); color: #fff; font-weight: 600; font-size: 17px; line-height: 1.3;
    padding: 12px 16px; flex: 1; margin-left: 6px; height: 72px;
  }
  .credits { margin-top: 18px; font-size: 17px; line-height: 1.4; }
  .fine-print {
    margin-top: 18px; background: var(--grey-band); color: var(--band-text);
    font-family: "Roboto Condensed", sans-serif; font-weight: 300; font-size: 13px; line-height: 1.4;
    padding: 12px 22px;
  }
  .footer { display: flex; justify-content: space-between; align-items: flex-end; margin-top: 22px; }
  .signup { font-size: 20px; font-weight: 600; text-transform: uppercase; letter-spacing: .5px; }
  .signup-row { display: flex; align-items: flex-end; gap: 10px; height: 34px; }
  .signup-row .line { width: 420px; border-bottom: 1px solid var(--rule); height: 22px; }
  .brand { display: flex; align-items: center; gap: 12px; color: var(--blue); font-size: 26px; font-weight: 600; }
  .brand-dot { width: 34px; height: 34px; border-radius: 50%; background: var(--blue); }
</style>
</head>
<body>
  <article class="postcard">
    <header class="header">
      <div class="title-block">
        <h2 class="announce">Announcing our newly redesigned</h2>
        <h1 class="program-title">Referral Program</h1>
      </div>
      <p class="tagline"><span>good people</span><span class="indent">know good people.</span></p>
    </header>

    <section class="intro">
      <p>Referrals are the <strong>lifeblood</strong> of our small business.</p>
      <p>We are <strong>incredibly grateful</strong> for your trust and recommendations over the years, and we want to show our gratitude. That's why we are introducing an exciting new way to earn more free treatment. Now you can:</p>
    </section>

    <section class="offers">
      <div class="offer">
        <div class="offer-amount"><span class="earn">EARN</span><span class="value">$25</span></div>
        <p class="offer-text">For every referral you make to our south Calgary location (Linden Grove)</p>
      </div>
      <div class="offer">
        <div class="offer-amount"><span class="earn">EARN</span><span class="value">$10</span></div>
        <p class="offer-text">For every referral you make to our north Calgary location (Harlow Ridge).</p>
      </div>
    </section>

    <p class="credits">Credits can be <strong>used for any service at either our north or south location</strong> and, in the spirit of community, <strong>credits are transferable</strong>. Refer 4 people to the south and you could gift someone a $100 gift card! Or, enjoy a well deserved, free treatment yourself.</p>

    <p class="fine-print">*Referral(s) must be brand new client(s) to the Brightpath Wellness Inc. practice, having never booked or attended an appointment at any Brightpath Wellness location. Referral must attend their appointment for you to be eligible for a referral credit. Referral credit value is dependent upon which Brightpath Wellness location your referral attends; you are eligible for a $10 credit for a referral to our north location (#4120 - 1180 Harlow Ridge Parkway NW); you are eligible for a $25 credit for a referral to our south location (#315 - 7740 Linden Grove Drive SE). We are really good at asking but please remind your referral to tell us it is YOU who we have to thank! Credit(s) may be redeemed as payment or partial payment for any service at any Brightpath Wellness location. Credits have no cash value and no expiry.</p>

    <footer class="footer">
      <div class="signup">
        <div class="signup-row"><span>Your name:</span><span class="line"></span></div>
        <div class="signup-row"><span>Referred by:</span><span class="line"></span></div>
      </div>
      <div class="brand"><span class="brand-dot"></span><span>Brightpath Wellness</span></div>
    </footer>
  </article>
</body>
</html>
```